依頼詳細
■依頼目的
本ブログの目的は、ミラボルト テクノサービスの認知拡大とブランディングとなります。
MTSの技術や最新動向への見解・取組を掲載する「MTS Tech ブログ」を立ち上げ、
中途採用 転職意向者 / ソリューション導入 検討者の意向を上げることを狙っております。

■デザインイメージ
ソラノート社運営ブログ「Buildnote.JX」
http://dev.soranote-example.jp/
制作注意点としまして、実装にはWordPressを使いますのでWordPressで実装が明らかにできないような
デザインは避けてください

■訴求ポイントの優先順位
1.ブログスペース
2.求人広告バナーエリア(自社のキャリア採用)

■ターゲット層
個人:中途採用 転職意向者
法人:ソリューション導入 検討者

■希望する色味
ミラボルトテクノサービスのトーン&マナーに合わせたもの
http://www.mts.mirabolt-example.co.jp/

■提供素材
ミラボルトテクノサービス:ロゴデーター

■納品ファイル
TOPページデザイン1点(PSDデータ)
ロゴの使用につきましては、添付のレギュレーションに従って作成をお願い致します。
デザインコンセプトにつきまして補足をさせて頂きます。TOPページのイメージとしまして一般的なブログ形式ではなく、デザインとレイアウトに関しましては最近のビジネスブログやキュレーションメディアのトレンドも考慮した先進性のあるデザインを考慮し、なおかつ読みやすい体裁での設計をお願いいたします。皆様からのご提案を心よりお待ちしております。よろしくお願いいたします。
ランサー様各位
この度は、たくさんの素晴らしいご提案を頂きましてありがとうございます。
さらにより多くの方からの魅力的なご応募を頂けるのではと思いまして
一週間延長の3/11(水)に延長することといたしました。
引き続き皆様からのご提案をお待ち申し上げます。

サイトの性質上、どうしても縦に長くなる中で、背景色に変化をつけることにより、情報ごとのブロックの認識がわかりやすくなったと感じます。また、単純なグリッドデザインでなくなり、変化がついていたところが決定したポイントになります。

この度は、皆様に当コンペにたくさんの素晴らしいデザインをご提案して頂きましてありがとうございました。

```html
<!DOCTYPE html>
<html lang="ja">
<head>
<meta charset="utf-8">
<title>MTS Tech ブログ</title>
<link href="https://fonts.googleapis.com/css2?family=Noto+Sans+JP:wght@400;500;700;900&family=Roboto:wght@400;500;700&display=swap" rel="stylesheet">
<style>
:root{
  --navy:#1b2f66;
  --navy-deep:#13224d;
  --blue:#1f7fcf;
  --blue-light:#e3eef9;
  --ink:#2b2b2b;
  --text:#444;
  --muted:#8a8f98;
  --line:#dde1e7;
  --bg:#eef0f3;
  --white:#fff;
  --tab:#2a2d33;
  --accent:#e8731c;
}
*{margin:0;padding:0;box-sizing:border-box}
html,body{width:1200px;height:2584px;overflow:hidden}
body{font-family:"Noto Sans JP",sans-serif;color:var(--text);background:var(--bg);font-size:12px;line-height:1.5}
.en{font-family:"Roboto",sans-serif}

/* header */
.site-header{height:64px;background:var(--white);display:flex;align-items:center;justify-content:space-between;padding:0 20px;border-bottom:1px solid var(--line)}
.brand{display:flex;align-items:center;gap:10px}
.brand-mark{width:22px;height:22px;background:var(--navy)}
.brand-name{font-weight:700;color:var(--navy);font-size:15px}
.blog-title{font-family:"Roboto",sans-serif;font-weight:700;color:var(--navy);font-size:15px;padding-left:14px;border-left:1px solid var(--line);margin-left:4px}
.search{width:300px;height:30px;border:1px solid var(--line);border-radius:3px;display:flex;align-items:center;justify-content:space-between;padding:0 10px;color:var(--muted);font-size:11px}

/* hero */
.hero{height:290px;display:flex;gap:10px;padding:0 20px;background:var(--white)}
.hero-main{position:relative;width:770px;height:280px;background:linear-gradient(110deg,#f7fbff 0%,#dfecf8 45%,#9fc6ea 100%)}
.hero-copy{position:absolute;left:30px;top:28px;font-size:33px;font-weight:900;color:var(--navy);line-height:1.35}
.hero-copy em{font-style:normal;color:var(--accent)}
.hero-more{position:absolute;left:30px;top:190px;font-size:12px;color:var(--navy);border-bottom:1px solid var(--navy)}
.hero-label{position:absolute;left:0;bottom:0;width:300px;height:40px;background:var(--blue);color:var(--white);font-weight:700;font-size:15px;display:flex;align-items:center;padding-left:16px}
.hero-side{width:380px;display:flex;flex-direction:column;gap:6px}
.hero-banner{flex:1;position:relative;background:linear-gradient(120deg,#1f3d7a,#4f7fb8);color:var(--white);padding:14px 16px;font-size:13px;font-weight:700;line-height:1.4}
.hero-banner:nth-child(2){background:linear-gradient(120deg,#2d5a94,#8fb6dc)}
.hero-banner:nth-child(3){background:linear-gradient(120deg,#16305e,#3c6aa3)}
.hero-banner small{display:block;font-weight:400;font-size:11px;opacity:.85}

/* layout */
.main{display:flex;gap:20px;padding:20px 20px 0}
.content{width:800px}
.sidebar{width:340px}
.section-title{font-family:"Roboto",sans-serif;font-weight:700;font-size:14px;color:var(--ink);margin:6px 0 8px}

/* cards */
.cat-tab{display:inline-block;background:var(--tab);color:var(--white);font-family:"Roboto",sans-serif;font-size:11px;padding:3px 12px}
.meta{display:flex;justify-content:space-between;align-items:center;color:var(--muted);font-size:11px;font-family:"Roboto",sans-serif}
.counts{display:flex;gap:6px}
.counts span{border:1px solid var(--line);padding:0 5px;border-radius:2px}
.post-title{font-weight:700;color:var(--ink);font-size:16px;line-height:1.4}
.excerpt{color:var(--muted);font-size:11.5px;line-height:1.6}
.tags{display:flex;gap:6px}
.tags span{font-size:10px;border:1px solid var(--line);padding:1px 8px;color:var(--text)}

.feature-list{display:flex;flex-direction:column;gap:14px;margin-bottom:20px}
.feature{display:flex;height:132px;background:var(--white)}
.feature-thumb{position:relative;width:200px;height:132px}
.feature-thumb .cat-tab{position:absolute;left:0;top:0}
.feature-body{flex:1;padding:10px 16px;display:flex;flex-direction:column;gap:5px}

.grid{display:grid;grid-template-columns:390px 390px;gap:20px}
.post{background:var(--white);height:360px;display:flex;flex-direction:column}
.post-thumb{height:172px}
.post-body{padding:12px 14px;display:flex;flex-direction:column;gap:7px}

.pager{display:flex;gap:6px;margin:40px 0 0;font-family:"Roboto",sans-serif}
.pager span{width:30px;height:30px;display:flex;align-items:center;justify-content:center;background:var(--white);border:1px solid var(--line);font-size:12px;color:var(--ink)}
.pager .current{background:var(--navy);color:var(--white);border-color:var(--navy)}

/* sidebar */
.ad{position:relative;height:262px;background:linear-gradient(160deg,#0f7fb8,#1b3f7a);color:var(--white);padding:18px 20px}
.ad-head{font-size:46px;font-weight:900;line-height:1}
.ad-head small{font-size:22px}
.ad-sub{margin-top:12px;font-size:13px;font-weight:500}
.ad-label{position:absolute;right:16px;top:16px;font-size:11px;background:rgba(255,255,255,.2);padding:2px 8px}
.ad-name{position:absolute;left:20px;bottom:18px;font-family:"Roboto",sans-serif;font-weight:700;font-size:20px;letter-spacing:.04em}
.box{background:var(--white);margin-top:16px;padding:12px 14px}
.box-title{background:var(--navy);color:var(--white);font-family:"Roboto",sans-serif;font-weight:700;font-size:13px;padding:6px 10px;margin:-12px -14px 12px}
.chip-row{display:flex;flex-wrap:wrap;gap:6px;margin-bottom:12px}
.chip{background:var(--navy);color:var(--white);font-size:11px;padding:3px 12px}
.chip.tag{background:var(--white);color:var(--text);border:1px solid var(--line)}
.sub-title{font-family:"Roboto",sans-serif;font-weight:700;color:var(--ink);margin-bottom:6px}
.job{border-bottom:1px solid var(--line);padding:9px 0}
.job h4{font-size:13px;color:var(--blue);font-weight:700}
.job p{font-size:11px;color:var(--muted)}
.job-tag{display:inline-block;background:var(--blue-light);color:var(--navy);font-size:10px;padding:0 6px;margin-right:4px}
.rank-tabs{display:flex;margin:-4px 0 10px}
.rank-tabs span{flex:1;text-align:center;padding:4px;font-size:12px;font-weight:700;background:var(--bg)}
.rank-tabs .on{background:var(--accent);color:var(--white)}
.rank{display:flex;gap:10px;padding:7px 0;border-bottom:1px solid var(--line);align-items:center}
.rank-no{width:20px;height:20px;background:var(--navy);color:var(--white);font-family:"Roboto",sans-serif;font-size:11px;display:flex;align-items:center;justify-content:center;flex:none}
.rank-thumb{width:60px;height:42px;flex:none}
.rank p{font-size:11.5px;color:var(--ink);line-height:1.4}
.banners{display:flex;flex-direction:column;gap:10px;margin-top:16px}
.banner{height:70px;color:var(--white);display:flex;align-items:center;padding:0 18px;font-weight:700;font-size:14px}

/* footer */
.site-footer{position:absolute;left:0;top:2364px;width:1200px;height:220px;background:var(--navy-deep);color:#c7cfe0;padding:34px 40px 0}
.footer-inner{display:flex;gap:60px}
.footer-brand{display:flex;align-items:center;gap:10px;width:300px;align-self:flex-start}
.footer-brand .brand-mark{background:var(--white);width:30px;height:30px}
.footer-brand span{color:var(--white);font-weight:700;font-size:18px}
.footer-nav{display:grid;grid-template-columns:repeat(4,170px);gap:8px 20px;font-size:11px}
.footer-nav a{color:#c7cfe0;text-decoration:none}
.footer-nav a::before{content:"›";margin-right:6px;color:var(--white)}
.copyright{position:absolute;left:0;bottom:18px;width:100%;text-align:center;font-size:10px;color:#8a95b2;font-family:"Roboto",sans-serif}
</style>
</head>
<body>

<header class="site-header">
  <div class="brand">
    <div class="brand-mark"></div>
    <span class="brand-name">ミラボルト テクノサービス</span>
    <span class="blog-title">MTS Tech Blog</span>
  </div>
  <div class="search">キーワードを入力してください
    <svg width="14" height="14" viewBox="0 0 14 14"><circle cx="6" cy="6" r="4.5" fill="none" stroke="#8a8f98" stroke-width="1.6"/><line x1="9.3" y1="9.3" x2="13" y2="13" stroke="#8a8f98" stroke-width="1.6"/></svg>
  </div>
</header>

<section class="hero">
  <div class="hero-main" role="img" aria-label="ビジネスマンと分析グラフのイメージ写真">
    <p class="hero-copy">法人営業における様々な課題を<br><em>「成約起点」</em>発想で解決する<br>アウトソーシングサービスです。</p>
    <span class="hero-more">詳しくはこちら ›</span>
    <div class="hero-label">セールスアウトソーシングサービス</div>
  </div>
  <div class="hero-side">
    <div class="hero-banner" role="img" aria-label="サーバールームの写真">ITインフラの構築・運用<small>クラウド移行から保守まで一貫対応</small></div>
    <div class="hero-banner" role="img" aria-label="オフィスで働く人の写真">システム開発から運用まで<small>業務に合わせた最適なソリューション</small></div>
    <div class="hero-banner" role="img" aria-label="ウェブ画面のイメージ写真">Web メディアソリューション<small>集客・運営・分析をトータル支援</small></div>
  </div>
</section>

<div class="main">
  <main class="content">
    <h2 class="section-title">Today's articles</h2>
    <div class="feature-list">
      <article class="feature">
        <div class="feature-thumb" role="img" aria-label="色とりどりの六角形アイコンが並ぶソーシャルメディアのイメージ" style="background:linear-gradient(135deg,#3aa0d8,#e8a23a 55%,#d84a5a)"><span class="cat-tab">Category</span></div>
        <div class="feature-body">
          <div class="meta"><span>2015.03.06</span><span class="counts"><span>10</span><span>24</span></span></div>
          <h3 class="post-title">ソーシャルメディアマーケティングとは誰のために存在しているのか？</h3>
          <p class="excerpt">企業が発信する情報と利用者が求める情報のずれを整理し、運用の目的をあらためて考えます。</p>
          <div class="tags"><span>SNS</span><span>マーケティング</span></div>
        </div>
      </article>
      <article class="feature">
        <div class="feature-thumb" role="img" aria-label="雲とアイコンで表したクラウドのイメージ" style="background:linear-gradient(135deg,#e9edf1,#b8c3ce)"><span class="cat-tab">Category</span></div>
        <div class="feature-body">
          <div class="meta"><span>2015.03.06</span><span class="counts"><span>10</span><span>24</span></span></div>
          <h3 class="post-title">ソーシャルメディアマーケティングとは誰のために存在しているのか？</h3>
          <p class="excerpt">クラウド時代の情報発信において、誰に何を届けるべきかを具体的な事例とともに解説します。</p>
          <div class="tags"><span>SNS</span><span>クラウド</span></div>
        </div>
      </article>
    </div>

    <h2 class="section-title">Previous day's articles</h2>
    <div class="grid">
      <article class="post"><span class="cat-tab">Category</span>
        <div class="post-thumb" role="img" aria-label="高層ビル群の写真" style="background:linear-gradient(180deg,#5d7ea3,#1f3350)"></div>
        <div class="post-body"><div class="meta"><span>2015.03.06</span><span class="counts"><span>10</span><span>24</span></span></div>
          <h3 class="post-title">アジャイル開発でソフトウェア開発のオーバーヘッドを削減する。</h3>
          <p class="excerpt">小さな単位で開発と検証を繰り返すことで、手戻りを減らし品質と速度を両立する方法を紹介します。</p>
          <div class="tags"><span>開発</span><span>手法</span></div></div></article>
      <article class="post"><span class="cat-tab">Category</span>
        <div class="post-thumb" role="img" aria-label="クラウドサービスのアイコン一覧" style="background:linear-gradient(135deg,#f4f4f4,#f2b36a)"></div>
        <div class="post-body"><div class="meta"><span>2015.03.06</span><span class="counts"><span>10</span><span>24</span></span></div>
          <h3 class="post-title">アジャイル開発でソフトウェア開発のオーバーヘッドを削減する。</h3>
          <p class="excerpt">小さな単位で開発と検証を繰り返すことで、手戻りを減らし品質と速度を両立する方法を紹介します。</p>
          <div class="tags"><span>開発</span><span>手法</span></div></div></article>
      <article class="post"><span class="cat-tab">Category</span>
        <div class="post-thumb" role="img" aria-label="検索サービスのロゴ画像" style="background:linear-gradient(135deg,#ffffff,#e6e9ee)"></div>
        <div class="post-body"><div class="meta"><span>2015.03.06</span><span class="counts"><span>10</span><span>24</span></span></div>
          <h3 class="post-title">アジャイル開発でソフトウェア開発のオーバーヘッドを削減する。</h3>
          <p class="excerpt">小さな単位で開発と検証を繰り返すことで、手戻りを減らし品質と速度を両立する方法を紹介します。</p>
          <div class="tags"><span>開発</span><span>手法</span></div></div></article>
      <article class="post"><span class="cat-tab">Category</span>
        <div class="post-thumb" role="img" aria-label="水辺のひなどりの写真" style="background:linear-gradient(180deg,#6f7a5a,#c9b86a)"></div>
        <div class="post-body"><div class="meta"><span>2015.03.06</span><span class="counts"><span>10</span><span>24</span></span></div>
          <h3 class="post-title">アジャイル開発でソフトウェア開発のオーバーヘッドを削減する。</h3>
          <p class="excerpt">小さな単位で開発と検証を繰り返すことで、手戻りを減らし品質と速度を両立する方法を紹介します。</p>
          <div class="tags"><span>開発</span><span>手法</span></div></div></article>
      <article class="post"><span class="cat-tab">Category</span>
        <div class="post-thumb" role="img" aria-label="ノートアプリのロゴ画像" style="background:linear-gradient(135deg,#4c4f55,#2e3035)"></div>
        <div class="post-body"><div class="meta"><span>2015.03.06</span><span class="counts"><span>10</span><span>24</span></span></div>
          <h3 class="post-title">アジャイル開発でソフトウェア開発のオーバーヘッドを削減する。</h3>
          <p class="excerpt">小さな単位で開発と検証を繰り返すことで、手戻りを減らし品質と速度を両立する方法を紹介します。</p>
          <div class="tags"><span>開発</span><span>手法</span></div></div></article>
      <article class="post"><span class="cat-tab">Category</span>
        <div class="post-thumb" role="img" aria-label="旅行検索サービスのロゴ画像" style="background:linear-gradient(135deg,#1d3b63,#0f2544)"></div>
        <div class="post-body"><div class="meta"><span>2015.03.06</span><span class="counts"><span>10</span><span>24</span></span></div>
          <h3 class="post-title">アジャイル開発でソフトウェア開発のオーバーヘッドを削減する。</h3>
          <p class="excerpt">小さな単位で開発と検証を繰り返すことで、手戻りを減らし品質と速度を両立する方法を紹介します。</p>
          <div class="tags"><span>開発</span><span>手法</span></div></div></article>
      <article class="post"><span class="cat-tab">Category</span>
        <div class="post-thumb" role="img" aria-label="人のアイコンがつながるネットワークのイメージ" style="background:linear-gradient(135deg,#f6f7f9,#9ec3e6)"></div>
        <div class="post-body"><div class="meta"><span>2015.03.06</span><span class="counts"><span>10</span><span>24</span></span></div>
          <h3 class="post-title">アジャイル開発でソフトウェア開発のオーバーヘッドを削減する。</h3>
          <p class="excerpt">小さな単位で開発と検証を繰り返すことで、手戻りを減らし品質と速度を両立する方法を紹介します。</p>
          <div class="tags"><span>開発</span><span>手法</span></div></div></article>
      <article class="post"><span class="cat-tab">Category</span>
        <div class="post-thumb" role="img" aria-label="ヘッドセットを着けたオペレーターの写真" style="background:linear-gradient(135deg,#e9e2da,#b89a80)"></div>
        <div class="post-body"><div class="meta"><span>2015.03.06</span><span class="counts"><span>10</span><span>24</span></span></div>
          <h3 class="post-title">アジャイル開発でソフトウェア開発のオーバーヘッドを削減する。</h3>
          <p class="excerpt">小さな単位で開発と検証を繰り返すことで、手戻りを減らし品質と速度を両立する方法を紹介します。</p>
          <div class="tags"><span>開発</span><span>手法</span></div></div></article>
    </div>
    <nav class="pager"><span class="current">1</span><span>2</span><span>3</span><span>4</span><span>5</span><span>6</span><span>7</span><span>…</span><span>100</span></nav>
  </main>

  <aside class="sidebar">
    <div class="ad" role="img" aria-label="求人サイトの広告バナー">
      <span class="ad-label">バナー</span>
      <p class="ad-head">好き<small>を</small><br>仕事に</p>
      <p class="ad-sub">Web、ゲーム、映像業界の仕事情報サイト</p>
      <p class="ad-name">LUMINA CREATIVEWORKS</p>
    </div>

    <div class="box">
      <h3 class="box-title">Category</h3>
      <div class="chip-row"><span class="chip">ITインフラ</span><span class="chip">Webメディア</span><span class="chip">システム開発</span><span class="chip">営業支援</span></div>
      <p class="sub-title">Tag</p>
      <div class="chip-row"><span class="chip tag">開発</span><span class="chip tag">SNS</span><span class="chip tag">クラウド</span><span class="chip tag">分析</span><span class="chip tag">セキュリティ</span><span class="chip tag">採用</span></div>
    </div>

    <div class="box">
      <h3 class="box-title">転職情報</h3>
      <div class="job"><h4>大規模分散処理エンジニア</h4><p><span class="job-tag">正社員</span>自社サービスの基盤設計・運用</p></div>
      <div class="job"><h4>大手通信会社</h4><p><span class="job-tag">正社員</span>インフラエンジニア（東京都）</p></div>
      <div class="job"><h4>大手自動車メーカー</h4><p><span class="job-tag">正社員</span>社内システムの企画・開発</p></div>
      <div class="job"><h4>Webディレクター</h4><p><span class="job-tag">正社員</span>メディア運営とコンテンツ企画</p></div>
      <div class="job"><h4>セールスエンジニア</h4><p><span class="job-tag">正社員</span>法人向けソリューション提案</p></div>
    </div>

    <div class="box">
      <h3 class="box-title">人気記事</h3>
      <div class="rank-tabs"><span class="on">アクセス</span><span>いいね</span></div>
      <div class="rank"><span class="rank-no">1</span><div class="rank-thumb" role="img" aria-label="記事サムネイル" style="background:#5d7ea3"></div><p>アジャイル開発でソフトウェア開発のオーバーヘッドを削減する。</p></div>
      <div class="rank"><span class="rank-no">2</span><div class="rank-thumb" role="img" aria-label="記事サムネイル" style="background:#e8a23a"></div><p>アジャイル開発でソフトウェア開発のオーバーヘッドを削減する。</p></div>
      <div class="rank"><span class="rank-no">3</span><div class="rank-thumb" role="img" aria-label="記事サムネイル" style="background:#9ec3e6"></div><p>アジャイル開発でソフトウェア開発のオーバーヘッドを削減する。</p></div>
      <div class="rank"><span class="rank-no">4</span><div class="rank-thumb" role="img" aria-label="記事サムネイル" style="background:#4c4f55"></div><p>アジャイル開発でソフトウェア開発のオーバーヘッドを削減する。</p></div>
      <div class="rank"><span class="rank-no">5</span><div class="rank-thumb" role="img" aria-label="記事サムネイル" style="background:#b89a80"></div><p>アジャイル開発でソフトウェア開発のオーバーヘッドを削減する。</p></div>
    </div>

    <div class="banners">
      <div class="banner" style="background:#2a6fb8">サイト改善に関するお役立ち情報</div>
      <div class="banner" style="background:#f2f4f7;color:var(--navy);border:1px solid var(--line)">Data Insight Blog</div>
      <div class="banner" style="background:#1b2f66">システム開発のご相談はこちら</div>
      <div class="banner" style="background:#3d8fd6">クラウド導入サポート</div>
      <div class="banner" style="background:#14305e">キャリア採用 エントリー受付中</div>
      <div class="banner" style="background:#e3eef9;color:var(--navy)">セミナー・イベント情報</div>
    </div>
  </aside>
</div>

<footer class="site-footer">
  <div class="footer-inner">
    <div class="footer-brand"><div class="brand-mark"></div><span>ミラボルト テクノサービス</span></div>
    <nav class="footer-nav">
      <a href="#">企業情報</a><a href="#">ソリューション</a><a href="#">導入事例</a><a href="#">採用情報</a>
      <a href="#">ITインフラ</a><a href="#">システム開発</a><a href="#">お知らせ</a><a href="#">お問い合わせ</a>
      <a href="#">Webメディア</a><a href="#">営業支援</a><a href="#">個人情報保護方針</a><a href="#">サイトマップ</a>
      <a href="#">MTS Tech ブログ</a><a href="#">セミナー</a><a href="#">ご利用規約</a>
    </nav>
  </div>
  <p class="copyright">Copyright © Mirabolt Techno Services, Ltd. All rights reserved.</p>
</footer>

</body>
</html>
```